Einzelne Suchwerk Landingpage
Suchwerk Landingpage für das Thema
„Vergleich von Private Rentenversicherungen“
Haupt Suchbegriffe für die die Landingpage verwendet werden soll:
-Private Rente
-Vergleich Private Rente
-Private Rentenversicherung
Mitbewerber:
Siehe Suchwerk Ergebnisse bei Eingabe obiger Suchbegriffe
Zielgruppe:
Alle Bundesbürger die sich mit privater Altersvorsorge beschäftigen.
Verstärkt Männer aber auch Frauen im Alter zwischen ca. 35-55 J.
Designanforderungen:
Spagat zwischen
Priorität I: ansprechenden des Besuchers auf emotionaler Ebene (Einbindung von Menschenbildern, etc.)
und
Priorität II: Ausdruck von Seriosität, Kompetenz und Unabhängigkeit
Als Beispiel-Designvorlagen von Mitbewerbern finde ich folgende Seite sehr ansprechend:
https://www1.ruhestand-kassenblick.de/ (hier ist mir nur das Formular zu groß, zu wenig Platz für Text)
Oder
http://www.geldlotse17.info/Sofortrente-Vergleich/index.html
(Design ist nicht so toll, aber klar strukturiert)
Vorlage für die Strukturierung der Seite:
Gute Erfahrungen was die Conversionsraten angeht habe ich mit der aktuell schon bestehenden Seite zum Thema „Rürup Rente“ gemacht.
www.kassenblick-basisplan-neu.de
Sicher ist diese was das Design angeht optimierungsfähig.
Was das Verhältnis Text/Formular angeht finde ich den Aufbau jedoch ganz gut bzw. hat sich die Seite bewährt. Die Unterseiten für Datenschutz und Impressum können ebenfalls übernommen werden.
Content
Der Text für die Seite ist hier hinterlegt:
www.wandoret.com/Inhalt_Text.docx
Formular:
Für das Formular könnten Sie ggf. auch den Quelltext der bestehenden Rürup Seite (s.o.) nutzen.
Das müsste dann nur minimal abgeändert werden.
www.wandoret.com/Formular.docx
Bei weiteren Rückfragen stehe ich gerne zur Verfügung.

```html
<!DOCTYPE html>
<html lang="de">
<head>
<meta charset="utf-8">
<title>Private Renten im Vergleich</title>
<link href="https://fonts.googleapis.com/css2?family=PT+Sans:wght@400;700&display=swap" rel="stylesheet">
<style>
:root{
  --page-bg:#e0eefa;
  --sheet:#ffffff;
  --brand:#4bb8d8;
  --brand-dark:#1e9fd0;
  --panel:#52bbd9;
  --panel-line:#6cc7e1;
  --info-top:#8eb4c2;
  --info-bot:#a7c6d1;
  --cream:#fdfbee;
  --text:#333333;
  --alert:#d9331a;
  --tick:#3fae2a;
  --link:#1f6fae;
  --btn-top:#ffd15a;
  --btn-bot:#f2a712;
}
*{box-sizing:border-box;margin:0;padding:0}
html,body{width:960px;height:1200px;overflow:hidden}
body{background:var(--page-bg);font-family:"PT Sans",Arial,sans-serif;color:var(--text)}
.sheet{position:absolute;left:106px;top:0;width:749px;height:1056px;background:var(--sheet)}
.topbar{position:absolute;left:0;top:0;width:749px;height:60px;background:linear-gradient(#ffffff,#eeeeee);border-bottom:1px solid #e2e2e2}
.site-name{position:absolute;right:22px;top:10px;font-size:32px;font-weight:700;color:var(--brand);letter-spacing:-.3px}
.hero-photo{position:absolute;left:8px;top:0;width:347px;height:223px;background:radial-gradient(ellipse at 35% 45%,#c9d9ea 0%,#e6edf4 55%,#ffffff 100%)}
.hero-title{position:absolute;left:376px;top:84px;width:370px;font-size:27px;line-height:30px;font-weight:400;color:var(--brand);white-space:nowrap}
.hero-alert{position:absolute;left:380px;top:152px;width:360px;font-size:13px;line-height:20px;color:var(--alert);white-space:nowrap}
.info-box{position:absolute;left:6px;top:223px;width:736px;height:111px;border-radius:5px;background:linear-gradient(var(--info-top),var(--info-bot));display:flex;padding:18px 20px 0 26px;gap:44px;color:#fff;font-size:10.5px;line-height:16px}
.info-box p{flex:1}
.claim{position:absolute;left:6px;top:343px;width:736px;height:45px;border-radius:5px;background:var(--panel);color:#fff;font-size:16.5px;line-height:45px;padding-left:27px}
.col-left{position:absolute;left:6px;top:388px;width:383px;font-size:10.5px;line-height:16px}
.cream{background:var(--cream);padding:14px 20px 10px 20px;height:347px}
.intro{max-width:270px}
.ticks{list-style:none;margin:10px 0 0 4px}
.ticks li{position:relative;padding-left:25px;height:19px;line-height:19px}
.ticks li svg{position:absolute;left:0;top:4px}
.h-sub{color:var(--brand-dark);font-weight:400}
.h-big{font-size:16.5px;line-height:24px;margin:18px 0 12px 3px}
.h-mid{font-size:13.5px;line-height:18px;margin:18px 0 0 1px}
.body-p{margin-left:3px}
.rest{padding:0 20px}
.col-right{position:absolute;left:396px;top:398px;width:346px}
.form-kicker{font-size:10.5px;margin-left:12px}
.form-head{font-size:16.5px;font-weight:400;color:var(--brand-dark);margin:7px 0 7px 12px}
.form-panel{background:var(--panel);border-radius:6px;color:#fff;font-size:10.5px;padding-bottom:12px}
.form-intro{padding:9px 16px 8px 16px;line-height:16px;border-bottom:1px solid var(--panel-line)}
.row{display:flex;align-items:center;height:25px;padding-left:14px;border-bottom:1px solid var(--panel-line);gap:4px}
.row label{margin-right:4px;white-space:nowrap}
.field{height:13px;background:#fff;border:1px solid #d8e8ee}
.pick{height:13px;background:#fff;border:1px solid #d8e8ee;color:#666;font-size:8px;line-height:11px;padding-left:3px;position:relative}
.pick::after{content:"";position:absolute;right:5px;top:4px;border:3px solid transparent;border-top:4px solid #555}
.privacy{padding:7px 14px 0 14px;line-height:17px;border-bottom:1px solid var(--panel-line);height:40px}
.check{display:flex;align-items:center;gap:7px;margin-left:3px}
.check .box{width:8px;height:8px;background:#fff;border:1px solid #aaa;display:block}
.submit{display:block;margin:11px auto 0;width:228px;height:28px;border-radius:4px;background:linear-gradient(var(--btn-top),var(--btn-bot));border:1px solid #e39a0a;color:#fff;font-family:inherit;font-size:18px;line-height:26px;text-align:center}
.after{margin-top:12px;font-size:10.5px;line-height:18.8px;padding-left:1px}
.footer{position:absolute;left:0;top:1003px;width:749px;height:53px;background:linear-gradient(#f6f6f6,#ffffff);border-top:1px solid #e6e6e6;font-size:10.5px;padding:20px 0 0 33px}
.footer a{color:var(--link);text-decoration:none;margin-right:14px}
</style>
</head>
<body>
<div class="sheet">
  <div class="topbar"><div class="site-name">ruhestand-kassenblick.de</div></div>
  <div class="hero-photo" role="img" aria-label="Foto eines lächelnden älteren Paares mit jüngeren Menschen im Hintergrund"></div>
  <h1 class="hero-title">Welche Private<br>Rentenversicherung nehmen?</h1>
  <p class="hero-alert">ACHTUNG!! Bis 31.12.2011 noch höhere Garantieverzinsung<br>für die gesamte Laufzeit sichern!!!</p>

  <div class="info-box">
    <p>Bevor Sie sich für die Private Rentenversicherung eines bestimmten Anbieters entscheiden, sollten Sie wissen, was vergleichbare Rentenversicherungen leisten. Welcher Anbieter für Sie attraktiv ist, kann nämlich je nach Eintrittsalter, Geschlecht oder Anlagementalität sehr variieren.</p>
    <p>Der Vergleich lohnt sich für Sie, denn gerade bei Privaten Rentenversicherungen gibt es riesige Unterschiede. Selbst wenn Ihnen die Differenz bei den Rentenergebnissen der Anbieter eher klein erscheint, können sich über die gesamte Rentenphase Unterschiede von 10.000 EUR und mehr ergeben.</p>
  </div>

  <div class="claim">Als unabhängige Vorsorgespezialisten holen wir mehr für Sie heraus!</div>

  <div class="col-left">
    <div class="cream">
      <p class="body-p intro">Fordern Sie jetzt Ihren kostenlosen und unverbindlichen Marktvergleich an. Unser Marktvergleich bietet mehr…</p>
      <ul class="ticks">
        <li><svg width="10" height="9" viewBox="0 0 10 9"><path d="M1 5l3 3 5-7" fill="none" stroke="var(--tick)" stroke-width="2.2"/></svg>Vergleich von über 45 Versicherungen</li>
        <li><svg width="10" height="9" viewBox="0 0 10 9"><path d="M1 5l3 3 5-7" fill="none" stroke="var(--tick)" stroke-width="2.2"/></svg>Klassische- und Fondsprodukte</li>
        <li><svg width="10" height="9" viewBox="0 0 10 9"><path d="M1 5l3 3 5-7" fill="none" stroke="var(--tick)" stroke-width="2.2"/></svg>Inkl. Direktversicherer</li>
        <li><svg width="10" height="9" viewBox="0 0 10 9"><path d="M1 5l3 3 5-7" fill="none" stroke="var(--tick)" stroke-width="2.2"/></svg>Inkl. berufsspezifischer Sonderrabatttarife</li>
        <li><svg width="10" height="9" viewBox="0 0 10 9"><path d="M1 5l3 3 5-7" fill="none" stroke="var(--tick)" stroke-width="2.2"/></svg>Tarife mit vergünstigten Kosten</li>
      </ul>
      <h2 class="h-sub h-big">Das gesetzliche Rentenniveau genügt nicht zur Grundversorgung!</h2>
      <p class="body-p" style="margin-left:5px">Mittlerweile ist es fast jedem klar. Die gesetzliche Rente wird nicht zur Grundversorgung ausreichen. Daher ist private Vorsorge unausweichlich. Jedoch unterschätzen die meisten Bundesbürger die Höhe der Rentenlücke im Alter.</p>
      <h3 class="h-sub h-mid">Folgende Faktoren werden meist unterschätzt:</h3>
      <ul class="ticks" style="margin-top:3px">
        <li><svg width="10" height="9" viewBox="0 0 10 9"><path d="M1 5l3 3 5-7" fill="none" stroke="var(--tick)" stroke-width="2.2"/></svg>Hohe Inflation</li>
      </ul>
    </div>
    <div class="rest">
      <ul class="ticks" style="margin-top:0">
        <li><svg width="10" height="9" viewBox="0 0 10 9"><path d="M1 5l3 3 5-7" fill="none" stroke="var(--tick)" stroke-width="2.2"/></svg>Immer weiter steigende Sozialabgaben</li>
        <li><svg width="10" height="9" viewBox="0 0 10 9"><path d="M1 5l3 3 5-7" fill="none" stroke="var(--tick)" stroke-width="2.2"/></svg>Insbesondere Krankenversicherungsausgaben</li>
        <li><svg width="10" height="9" viewBox="0 0 10 9"><path d="M1 5l3 3 5-7" fill="none" stroke="var(--tick)" stroke-width="2.2"/></svg>Steigende Lebenshaltungskosten</li>
        <li><svg width="10" height="9" viewBox="0 0 10 9"><path d="M1 5l3 3 5-7" fill="none" stroke="var(--tick)" stroke-width="2.2"/></svg>Pflegekosten</li>
        <li><svg width="10" height="9" viewBox="0 0 10 9"><path d="M1 5l3 3 5-7" fill="none" stroke="var(--tick)" stroke-width="2.2"/></svg>etc.</li>
      </ul>
      <h3 class="h-sub h-mid" style="margin-left:3px">Die Vorteile der privaten Rentenversicherung:</h3>
      <ul class="ticks" style="margin-top:5px">
        <li><svg width="10" height="9" viewBox="0 0 10 9"><path d="M1 5l3 3 5-7" fill="none" stroke="var(--tick)" stroke-width="2.2"/></svg>Maximale Flexibilität</li>
        <li><svg width="10" height="9" viewBox="0 0 10 9"><path d="M1 5l3 3 5-7" fill="none" stroke="var(--tick)" stroke-width="2.2"/></svg>Beliebige Vererbbarkeit</li>
        <li><svg width="10" height="9" viewBox="0 0 10 9"><path d="M1 5l3 3 5-7" fill="none" stroke="var(--tick)" stroke-width="2.2"/></svg>Wahlrecht Kapital oder Rente</li>
        <li><svg width="10" height="9" viewBox="0 0 10 9"><path d="M1 5l3 3 5-7" fill="none" stroke="var(--tick)" stroke-width="2.2"/></svg>Garantierte lebenslange Rente</li>
        <li><svg width="10" height="9" viewBox="0 0 10 9"><path d="M1 5l3 3 5-7" fill="none" stroke="var(--tick)" stroke-width="2.2"/></svg>Abgeltungssteuerfrei sparen</li>
        <li><svg width="10" height="9" viewBox="0 0 10 9"><path d="M1 5l3 3 5-7" fill="none" stroke="var(--tick)" stroke-width="2.2"/></svg>Attraktive Rendite mit Garantieverzinsung</li>
      </ul>
    </div>
  </div>

  <div class="col-right">
    <p class="form-kicker">Private Rente: Anbieter &amp; Tarife</p>
    <h2 class="form-head">Private Renten im Vergleich</h2>
    <div class="form-panel">
      <p class="form-intro">Private Renten im VergleichFordern Sie hier Ihren kostenlosen Versicherungsvergleich an.</p>
      <div class="row"><label>Anlagebetrag (€/Zahlart):</label><span class="field" style="width:84px"></span><span class="pick" style="width:84px">monatlich</span></div>
      <div class="row"><label>Rentenauszahlung: im Alter von</label><span class="field" style="width:84px"></span><span style="margin-left:3px">Jahren</span></div>
      <div class="row"><label>Bruttoeinkommen (€/Jahr):</label><span class="field" style="width:84px"></span></div>
      <div class="row" style="height:28px"><label>Kinder:</label><span class="pick" style="width:88px">Bitte auswählen</span><label style="margin-left:8px">Familienstand:</label><span class="pick" style="width:88px">Bitte auswählen</span></div>
      <div class="row"><label>Beruf, Berufsstatus:</label><span class="field" style="width:84px"></span><span class="pick" style="width:84px">angesteller</span></div>
      <div class="row"><label>Geburtsdatum:</label><span class="pick" style="width:32px">Tag</span><span class="pick" style="width:42px">Monat</span><span class="pick" style="width:41px">Jahr</span></div>
      <div class="row"><label>Straße, Hausnummer:</label><span class="field" style="width:204px"></span></div>
      <div class="row"><label>PLZ, Wohnort:</label><span class="field" style="width:32px"></span><span class="field" style="width:201px"></span></div>
      <div class="row"><label>Tel.-Nr. / Erreichbarkeit:</label><span class="field" style="width:106px"></span><span class="pick" style="width:87px">Ganztags</span></div>
      <div class="row"><label>E-Mail-Adresse:</label><span class="field" style="width:204px"></span></div>
      <div class="privacy">
        <p>Sicherheit &amp; Datenschutz Ihre Daten sind sicher und geschützt.</p>
        <div class="check"><svg class="box" width="8" height="8" viewBox="0 0 8 8"><path d="M1.5 4l2 2 3-5" fill="none" stroke="#6a4fa0" stroke-width="1.3"/></svg>Ich habe den Datenschutz gelesen und akzeptiert.</div>
      </div>
      <div class="submit">KOSTENFREI VERGLEICH</div>
    </div>
    <p class="after">Sie haben Ihre Angaben gemacht. So geht es weiter:<br>In Kürze erhalten Sie Ihren Versicherungsvergleich.<br>Der Vergleich wird softwaregestützt von unseren qualifizierten Spezialisten erstellt.<br>Dieser Service ist kostenfrei. Wir bitten Sie nur ernsthafte und vollständige Angaben zu machen, da ansonsten kein Vergleich erstellt werden kann. Bei weiteren Fragen stehen Ihnen unsere Experten via Onlineberatung zur Verfügung.</p>
  </div>

  <footer class="footer"><a href="#">Impressum</a><a href="#">Datenschutz</a></footer>
</div>
</body>
</html>
```